'Tarvel' a financial/crypto-currency exchange in the middle east

On the card we need 1) Name 2) title 3) email address 4) phone number using the same colors and theme as the logo. On one side we just want the logo and we want the whole card to be in blue (same blue as logo) with the logo in the back being white.
Industry/Entity Type
Financial

```html
<!DOCTYPE html>
<html lang="en">
<head>
<meta charset="utf-8">
<title>Tarvel Business Card</title>
<link rel="stylesheet" href="https://fonts.googleapis.com/css2?family=Poppins:wght@400;600;700&display=swap">
<style>
  :root {
    --brand-blue: #1b8fcf;
    --brand-blue-soft: #3998d3;
    --card-white: #ffffff;
    --backdrop: #1f2024;
    --ink-light: #ffffff;
  }
  * { margin: 0; padding: 0; box-sizing: border-box; }
  html, body {
    width: 1200px;
    height: 800px;
    overflow: hidden;
    background: var(--backdrop);
    font-family: "Poppins", sans-serif;
  }
  .stage {
    width: 1200px;
    height: 800px;
    display: flex;
    align-items: center;
    justify-content: center;
    gap: 40px;
  }
  .card {
    width: 525px;
    height: 300px;
    position: relative;
    overflow: hidden;
    box-shadow: 0 18px 40px rgba(0, 0, 0, 0.45);
  }
  .card-front {
    background: var(--card-white);
    display: flex;
    align-items: center;
    justify-content: center;
    gap: 16px;
  }
  .brand-dot {
    width: 64px;
    height: 64px;
    border-radius: 50%;
    background: var(--brand-blue);
    flex-shrink: 0;
  }
  .brand-name {
    color: var(--brand-blue);
    font-weight: 700;
    font-size: 52px;
    letter-spacing: 0.5px;
    line-height: 1;
  }
  .card-back {
    background: var(--brand-blue);
    display: flex;
    align-items: center;
    justify-content: center;
  }
  .back-ring {
    position: absolute;
    inset: 0;
    width: 100%;
    height: 100%;
  }
  .contact-block {
    position: relative;
    text-align: center;
    color: var(--ink-light);
  }
  .person-name {
    font-weight: 700;
    font-size: 20px;
    line-height: 1.1;
  }
  .person-title {
    font-weight: 400;
    font-size: 13px;
    margin-bottom: 10px;
  }
  .contact-line {
    font-weight: 400;
    font-size: 13px;
    letter-spacing: 0.2px;
  }
  .contact-line strong { font-weight: 600; }
</style>
</head>
<body>
  <main class="stage">
    <section class="card card-front" aria-label="Card front">
      <span class="brand-dot"></span>
      <span class="brand-name">Tarvel</span>
    </section>

    <section class="card card-back" aria-label="Card back">
      <svg class="back-ring" viewBox="0 0 525 300" aria-hidden="true">
        <circle cx="262" cy="150" r="190" fill="var(--brand-blue-soft)" opacity="0.55"/>
        <circle cx="262" cy="150" r="168" fill="var(--brand-blue)" opacity="0.35"/>
      </svg>
      <div class="contact-block">
        <p class="person-name">Omar Haddad</p>
        <p class="person-title">Founder</p>
        <p class="contact-line"><strong>P:</strong> (555) 210-4830 | <strong>E:</strong>info@tarvelmail.com</p>
      </div>
    </section>
  </main>
</body>
</html>
```